Australian Web Design company needs a business card design

We need a business card design for a Sydney based Web Design/Development company called "Tall Pine Web Design". We design, build and deploy websites for small to medium sized businesses. The final design should be clean and communicate that we are a professional and supportive company.
I'd like the Icon to be abstract. Something that embodies the power of the internet, needs to be clean/professional and show that we are human and that we support our customers. Hope that helps.
Target Market(s)
All small to medium businesses
Industry/Entity Type
Business
Contact Information for Business Card
Martin Forbes
Tall Pine Web Design
17 Wattle Grove Road
West Kelsworth
NSW 2250
0438 527 064
martin@tallpinewebdesign.com.au
www.tallpinewebdesign.com.au

```html
<!DOCTYPE html>
<html lang="en">
<head>
<meta charset="utf-8">
<title>Tall Pine Web Design – Business Card</title>
<link rel="stylesheet" href="https://fonts.googleapis.com/css2?family=Noto+Serif:ital,wght@0,400;0,700;1,400&family=Open+Sans:wght@400;700&display=swap">
<style>
  :root {
    --backdrop: #e4e5e7;
    --card-light: #dfe0e2;
    --card-dark: #1d1b1c;
    --ink: #2a2a2a;
    --ink-soft: #4a4a4a;
    --accent-red: #d3262b;
    --white: #f4f4f4;
  }
  * { box-sizing: border-box; margin: 0; padding: 0; }
  html, body {
    width: 1200px; height: 1000px; overflow: hidden;
    background: var(--backdrop);
  }
  .canvas { position: relative; width: 1200px; height: 1000px; }

  .card {
    position: absolute;
    width: 520px; height: 317px;
    border-radius: 4px;
    overflow: hidden;
    box-shadow: 0 6px 18px rgba(0,0,0,0.12);
  }

  /* Front side */
  .card--front { left: 110px; top: 110px; background: var(--card-light); }
  .card--front .network-panel {
    position: absolute; right: 0; top: 0;
    width: 200px; height: 100%;
    background: linear-gradient(160deg, rgba(211,38,43,0.10), rgba(60,60,60,0.14) 60%, rgba(211,38,43,0.08));
  }
  .brand {
    position: absolute; left: 32px; top: 30px;
    font-family: "Noto Serif", serif;
  }
  .brand__name {
    font-size: 30px; font-weight: 400; color: var(--ink);
    letter-spacing: -0.5px; line-height: 1;
  }
  .brand__tag {
    font-family: "Open Sans", sans-serif;
    font-size: 9px; letter-spacing: 1px; color: var(--ink-soft);
    margin-top: 4px;
  }
  .person {
    position: absolute; left: 32px; top: 132px;
  }
  .person__name {
    font-family: "Open Sans", sans-serif;
    font-weight: 700; font-size: 17px; color: var(--ink);
  }
  .person__role {
    font-family: "Noto Serif", serif;
    font-style: italic; font-size: 11px; color: var(--ink-soft);
    margin-top: 2px;
  }
  .contact {
    position: absolute; left: 32px; top: 200px;
    font-family: "Noto Serif", serif;
    font-size: 11px; line-height: 1.45; color: var(--ink-soft);
    list-style: none;
  }

  /* Back side */
  .card--back { left: 570px; top: 560px; background: var(--card-dark); }
  .card--back .network-panel {
    position: absolute; left: 0; top: 0;
    width: 100%; height: 150px;
    background: linear-gradient(180deg, rgba(211,38,43,0.22), rgba(200,200,200,0.08) 70%, rgba(29,27,28,0));
  }
  .wordmark {
    position: absolute; left: 150px; top: 170px;
    font-family: "Noto Serif", serif;
    font-size: 58px; font-weight: 400; color: var(--white);
    letter-spacing: -1px;
  }
</style>
</head>
<body>
<main class="canvas">

  <section class="card card--front" aria-label="Business card front">
    <div class="network-panel" role="img" aria-label="Network of connected lines and red nodes"></div>
    <div class="brand">
      <div class="brand__name">TallPine</div>
      <div class="brand__tag">WEB DESIGN</div>
    </div>
    <div class="person">
      <div class="person__name">Martin Forbes</div>
      <div class="person__role">function</div>
    </div>
    <ul class="contact">
      <li>Tall Pine Web Design</li>
      <li>17 Wattle Grove Road West Kelsworth NSW</li>
      <li>phone: 0438 527 064</li>
      <li>martin@tallpinewebdesign.com.au</li>
      <li>www.tallpinewebdesign.com.au</li>
    </ul>
  </section>

  <section class="card card--back" aria-label="Business card back">
    <div class="network-panel" role="img" aria-label="Network of connected lines and red nodes"></div>
    <div class="wordmark">TallPine</div>
  </section>

</main>
</body>
</html>
```